Package deal - Corvane Linen & Laundry

We had a great little logo for the start up of our small business. We have just received word from lawyers that a term we used was trademarked. We now have a new title and need to edit our logo asap plus...
Letterhead - For Outlook and Word
Business Card
Email Signature - for Outlook
Our tagline will now be "We keep the dirt. You get the clean"
Email - tovi@corvanelnl.example
Phone - +61482 915 264
Website - http://corvanelnl.example
Location - 14 Quindle Court, Yallup 6391, Western Australia
Title - General Manager
Name - Tovi Renkaro
Target Market(s)
Australian hospitality businesses requiring prompt, professional and personalized service. This service is dedicated to hiring and laundering of linen for commercial businesses such as hotels, restaurants, bed and breakfasts. We intend for it to branch out to personal items and cleaning in the future.
Look and feel
Each slider illustrates characteristics of the customer's brand and the style your logo design should communicate.

```html
<!DOCTYPE html>
<html lang="en">
<head>
<meta charset="utf-8">
<title>Corvane Linen &amp; Laundry – Stationery Options</title>
<link href="https://fonts.googleapis.com/css2?family=Source+Sans+3:wght@300;400;600;700&display=swap" rel="stylesheet">
<style>
  :root {
    --stage: #6e4b33;
    --paper: #ffffff;
    --paper-shade: #eef0f2;
    --brand-green: #4aa838;
    --brand-blue: #1c5ea8;
    --brand-blue-dark: #154a8a;
    --ink: #333a40;
    --ink-soft: #6b7178;
    --rule: #555b61;
    --ghost: #dfe5ee;
    --label: #ffffff;
  }
  * { box-sizing: border-box; margin: 0; padding: 0; }
  html, body { width: 1200px; height: 380px; overflow: hidden; }
  body {
    background: var(--stage);
    font-family: "Source Sans 3", "Helvetica Neue", Arial, sans-serif;
    color: var(--ink);
    position: relative;
  }
  .sheet, .envelope, .card {
    position: absolute;
    background: linear-gradient(160deg, var(--paper) 55%, var(--paper-shade));
    overflow: hidden;
  }
  .sheet { top: 16px; width: 254px; height: 326px; }
  .sheet--plain { left: 14px; }
  .sheet--letter { left: 292px; }
  .sheet--fax { left: 574px; }

  .brand {
    position: absolute;
    display: flex; align-items: center; gap: 4px;
  }
  .brand__dot {
    width: 10px; height: 10px; border-radius: 50%;
    background: var(--brand-blue);
    flex: none;
  }
  .brand__name {
    color: var(--brand-green);
    font-weight: 700;
    font-size: 10px;
    line-height: 1;
    width: 68px;
  }
  .sheet .brand { top: 10px; left: 10px; }
  .sheet--plain .brand { left: 88px; }

  .contact {
    position: absolute; top: 10px; left: 196px;
    font-size: 4.4px; line-height: 6px; color: var(--ink-soft);
  }
  .contact__row { display: flex; align-items: center; gap: 2px; white-space: nowrap; }
  .contact__icon { width: 4px; height: 4px; border-radius: 50%; background: var(--brand-green); flex: none; }
  .contact__gap { height: 2px; }

  .ghost-name {
    position: absolute; left: 8px; bottom: 30px;
    font-size: 40px; font-weight: 700; line-height: 1;
    color: var(--ghost);
  }
  .footer-contact {
    position: absolute; bottom: 6px; left: 0; right: 0;
    text-align: center; font-size: 4.4px; line-height: 6px; color: var(--ink-soft);
  }
  .footer-contact__line { display: flex; justify-content: center; gap: 6px; }
  .footer-contact__item { display: inline-flex; align-items: center; gap: 2px; }

  .wave { position: absolute; left: 0; bottom: 0; width: 100%; display: block; }
  .sheet .wave { height: 46px; }
  .tagline {
    position: absolute; right: 10px; bottom: 19px;
    font-size: 5px; line-height: 6px; font-weight: 600; color: var(--brand-blue-dark);
    white-space: nowrap;
  }

  .fax__title {
    position: absolute; top: 58px; left: 14px;
    font-size: 17px; font-weight: 300; color: var(--ink); letter-spacing: 0.5px;
  }
  .fax__fields {
    position: absolute; top: 82px; left: 14px; width: 228px;
    display: grid; grid-template-columns: 1fr 1fr; column-gap: 14px; row-gap: 6px;
  }
  .fax__field {
    font-size: 4.6px; color: var(--ink);
    border-bottom: 0.6px solid var(--rule);
    padding-bottom: 1px; height: 8px;
  }
  .fax__field--left { width: 120px; }
  .fax__checks {
    position: absolute; top: 158px; left: 14px;
    display: flex; gap: 11px; font-size: 4.6px; color: var(--ink);
  }
  .fax__check { display: flex; align-items: center; gap: 3px; }
  .fax__box { width: 6px; height: 6px; border: 0.6px solid var(--rule); }

  .label {
    position: absolute; top: 350px;
    font-size: 18px; font-weight: 400; color: var(--label);
  }

  .envelope { height: 108px; }
  .envelope--back { left: 884px; top: 4px; width: 274px; }
  .envelope--open { left: 846px; top: 60px; width: 280px; height: 126px; }
  .envelope--front { left: 876px; top: 116px; width: 282px; height: 126px; }
  .envelope__flap { position: absolute; left: 0; top: 0; width: 100%; height: 52px; display: block; }
  .envelope__flap-name {
    position: absolute; top: 14px; left: 140px;
    font-size: 11px; font-weight: 700; color: var(--paper); line-height: 1;
  }
  .envelope--open .envelope__flap-name { top: 36px; left: 120px; color: var(--brand-blue); }
  .envelope--front .brand { top: 12px; left: 14px; }
  .envelope--front .brand__name { font-size: 13px; width: 90px; }
  .envelope--front .brand__dot { width: 12px; height: 12px; }
  .envelope__address {
    position: absolute; top: 44px; left: 14px; font-size: 4.6px; color: var(--ink-soft);
  }
  .envelope .wave { height: 44px; }
  .envelope__web {
    position: absolute; right: 18px; bottom: 18px;
    font-size: 4.6px; line-height: 6px; letter-spacing: 0.6px; color: var(--ink-soft);
  }

  .card { top: 270px; width: 144px; height: 82px; border-radius: 8px; }
  .card--front { left: 872px; }
  .card--back { left: 1030px; }
  .card .brand { top: 8px; left: 30px; }
  .card .brand__name { font-size: 10px; width: 80px; }
  .card--back .brand { left: 32px; top: 10px; }
  .card__person {
    position: absolute; top: 34px; left: 6px; width: 66px;
    text-align: right; font-size: 4.4px; line-height: 5.6px; color: var(--ink-soft);
  }
  .card__name { font-size: 5.8px; font-weight: 700; color: var(--brand-green); }
  .card__contact { position: absolute; top: 42px; left: 78px; font-size: 4.4px; line-height: 6px; color: var(--ink-soft); }
  .card .wave { height: 16px; }
  .card__tagline {
    position: absolute; top: 50px; left: 0; right: 0; text-align: center;
    font-size: 5.6px; font-weight: 600; color: var(--brand-blue);
  }
  .card__web {
    position: absolute; top: 64px; left: 0; right: 0; text-align: center;
    font-size: 4.4px; letter-spacing: 0.6px; color: var(--ink-soft);
  }
</style>
</head>
<body>

<svg width="0" height="0" style="position:absolute" aria-hidden="true">
  <defs>
    <symbol id="brand-wave" viewBox="0 0 254 46" preserveAspectRatio="none">
      <path d="M0 4 C80 10 180 26 254 30 L254 46 L0 46 Z" fill="#4aa838"/>
      <path d="M0 10 C90 16 180 30 254 34 L254 46 L0 46 Z" fill="#ffffff"/>
      <path d="M0 13 C90 20 180 33 254 36 L254 46 L0 46 Z" fill="#1c5ea8"/>
      <path d="M140 46 C200 44 230 40 254 37 L254 46 Z" fill="#4aa838"/>
    </symbol>
  </defs>
</svg>

<!-- Letterhead option 1 -->
<section class="sheet sheet--plain" aria-label="Letterhead option 1">
  <div class="brand"><span class="brand__dot"></span><span class="brand__name">Corvane Linen &amp; Laundry</span></div>
  <div class="ghost-name" aria-hidden="true">Corvane</div>
  <div class="footer-contact">
    <div>14 Quindle Court, Yallup 6391, Western Australia</div>
    <div class="footer-contact__line">
      <span class="footer-contact__item"><span class="contact__icon"></span>+61482 915 264</span>
      <span class="footer-contact__item"><span class="contact__icon"></span>tovi@corvanelnl.example</span>
      <span class="footer-contact__item"><span class="contact__icon"></span>www.corvanelnl.example</span>
    </div>
  </div>
</section>

<!-- Letterhead option 2 -->
<section class="sheet sheet--letter" aria-label="Letterhead option 2">
  <div class="brand"><span class="brand__dot"></span><span class="brand__name">Corvane Linen &amp; Laundry</span></div>
  <div class="contact">
    <div class="contact__row"><span class="contact__icon"></span>+61482 915 264</div>
    <div class="contact__row"><span class="contact__icon"></span>tovi@corvanelnl.example</div>
    <div class="contact__row"><span class="contact__icon"></span>www.corvanelnl.example</div>
    <div class="contact__gap"></div>
    <div>14 Quindle Court, Yallup 6391</div>
    <div>Western Australia</div>
  </div>
  <svg class="wave" aria-hidden="true"><use href="#brand-wave"/></svg>
  <div class="tagline">We Keep The Dirt. You Get The Clean</div>
</section>

<!-- Fax sheet option 3 -->
<section class="sheet sheet--fax" aria-label="Fax sheet option 3">
  <div class="brand"><span class="brand__dot"></span><span class="brand__name">Corvane Linen &amp; Laundry</span></div>
  <div class="contact">
    <div class="contact__row"><span class="contact__icon"></span>+61482 915 264</div>
    <div class="contact__row"><span class="contact__icon"></span>tovi@corvanelnl.example</div>
    <div class="contact__row"><span class="contact__icon"></span>www.corvanelnl.example</div>
    <div class="contact__gap"></div>
    <div>14 Quindle Court, Yallup 6391</div>
    <div>Western Australia</div>
  </div>
  <h1 class="fax__title">FAX</h1>
  <div class="fax__fields">
    <div class="fax__field fax__field--left">To :</div><div class="fax__field">From :</div>
    <div class="fax__field fax__field--left">Fax :</div><div class="fax__field">Pages :</div>
    <div class="fax__field fax__field--left">Phone :</div><div class="fax__field">Date :</div>
    <div class="fax__field fax__field--left">Re :</div><div class="fax__field">CC :</div>
  </div>
  <div class="fax__checks">
    <span class="fax__check"><span class="fax__box"></span>Urgent</span>
    <span class="fax__check"><span class="fax__box"></span>For Review</span>
    <span class="fax__check"><span class="fax__box"></span>Please Comment</span>
    <span class="fax__check"><span class="fax__box"></span>Please Reply</span>
    <span class="fax__check"><span class="fax__box"></span>Please Recycle</span>
  </div>
  <svg class="wave" aria-hidden="true"><use href="#brand-wave"/></svg>
</section>

<div class="label" style="left:96px">Option-1</div>
<div class="label" style="left:374px">Option-2</div>
<div class="label" style="left:656px">Option-3</div>

<!-- Envelopes -->
<section class="envelope envelope--back" aria-label="Envelope back">
  <svg class="envelope__flap" viewBox="0 0 274 52" preserveAspectRatio="none" aria-hidden="true">
    <path d="M0 0 L274 0 L274 10 C200 40 160 52 137 52 C114 52 74 40 0 10 Z" fill="#1c5ea8"/>
  </svg>
  <span class="envelope__flap-name">Corvane</span>
</section>

<section class="envelope envelope--open" aria-label="Envelope flap open">
  <svg class="envelope__flap" viewBox="0 0 280 52" preserveAspectRatio="none" aria-hidden="true">
    <path d="M6 2 C6 14 20 22 40 28 L120 48 C132 52 148 52 160 48 L240 28 C260 22 274 14 274 2" fill="none" stroke="#555b61" stroke-width="0.8"/>
  </svg>
  <span class="envelope__flap-name">Corvane</span>
</section>

<section class="envelope envelope--front" aria-label="Envelope front">
  <div class="brand"><span class="brand__dot"></span><span class="brand__name">Corvane Linen &amp; Laundry</span></div>
  <div class="envelope__address">14 Quindle Court, Yallup 6391, Western Australia</div>
  <svg class="wave" aria-hidden="true"><use href="#brand-wave"/></svg>
  <div class="envelope__web">www.corvanelnl.example</div>
</section>

<!-- Business cards -->
<section class="card card--front" aria-label="Business card front">
  <div class="brand"><span class="brand__dot"></span><span class="brand__name">Corvane Linen &amp; Laundry</span></div>
  <div class="card__person">
    <div class="card__name">Tovi Renkaro</div>
    <div>General Manager</div>
    <div>14 Quindle Court, Yallup 6391</div>
    <div>Western Australia</div>
  </div>
  <div class="card__contact">
    <div class="contact__row"><span class="contact__icon"></span>+61482 915 264</div>
    <div class="contact__row"><span class="contact__icon"></span>tovi@corvanelnl.example</div>
    <div class="contact__row"><span class="contact__icon"></span>www.corvanelnl.example</div>
  </div>
  <svg class="wave" aria-hidden="true"><use href="#brand-wave"/></svg>
</section>

<section class="card card--back" aria-label="Business card back">
  <div class="brand"><span class="brand__dot"></span><span class="brand__name">Corvane Linen &amp; Laundry</span></div>
  <div class="card__tagline">We Keep The Dirt. You Get The Clean</div>
  <div class="card__web">www.corvanelnl.example</div>
</section>

</body>
</html>
```